Crimson Ledger.com is wanting to create a Facebook Ad to attract buyers to come to their website. We are wanting buyers to register for free and create an account on Crimson Ledger. com. We want to increase the number of buyers by posting an ad on Facebook groups. The buyer will click the link to our websites registration page.
https://www.crimsonledger.com/account/users/register

Semi Trucks
Semi Trailers
Construction Equipment
Farm Equipment
Trailers
ATV/UTV
Boats
RVs

```html
<!DOCTYPE html>
<html lang="en">
<head>
<meta charset="utf-8">
<title>Crimson Ledger – Run Salvage Auction Now</title>
<link rel="stylesheet" href="https://fonts.googleapis.com/css2?family=Archivo+Black&family=Oswald:wght@500&family=Roboto:wght@700&display=swap">
<style>
  :root{
    --bg-dark:#2b2b2b;
    --bg-mid:#3d3d3d;
    --orange:#e2621f;
    --orange-deep:#c24d12;
    --silver-hi:#ffffff;
    --silver-lo:#9a9a9a;
    --card-face:#e9e9e9;
    --card-edge:#bdbdbd;
    --label-ink:#2a2a2a;
    --chevron:#5c5c5c;
  }
  html,body{margin:0;padding:0;overflow:hidden;}
  body{width:1200px;height:1200px;}
  .ad{
    position:relative;width:1200px;height:1200px;overflow:hidden;
    background:radial-gradient(ellipse at 50% 45%, var(--bg-mid) 0%, var(--bg-dark) 75%);
  }
  .headline{
    position:absolute;left:0;right:0;top:52px;margin:0;text-align:center;
    font-family:"Archivo Black",sans-serif;font-weight:400;
    font-size:112px;line-height:1.0;letter-spacing:1px;
    background:linear-gradient(180deg,var(--silver-hi) 0%,#d6d6d6 45%,var(--silver-lo) 100%);
    -webkit-background-clip:text;background-clip:text;color:transparent;
  }
  .chevrons{position:absolute;left:50px;top:289px;width:52px;height:312px;}
  .card{
    position:absolute;box-sizing:border-box;padding:8px 8px 0;
    background:linear-gradient(180deg,#f4f4f4,var(--card-face) 60%,#cfcfcf);
    border:2px solid var(--card-edge);border-radius:6px;
    box-shadow:0 6px 14px rgba(0,0,0,.55);
    display:flex;flex-direction:column;
  }
  .card-photo{flex:1;border-radius:2px;}
  .card-label{
    height:58px;display:flex;align-items:center;justify-content:center;
    font-family:"Oswald",sans-serif;font-weight:500;font-size:29px;
    color:var(--label-ink);letter-spacing:-.5px;white-space:nowrap;
  }
  .card-construction{left:147px;top:356px;width:284px;height:268px;}
  .card-semi{left:444px;top:291px;width:312px;height:289px;}
  .card-farm{left:769px;top:356px;width:284px;height:268px;}
  .card-atv{left:49px;top:641px;width:245px;height:231px;}
  .card-atv .card-label,.card-trailers .card-label{height:52px;font-size:27px;}
  .card-trailers{left:906px;top:641px;width:246px;height:231px;}
  .photo-construction{background:linear-gradient(160deg,#6c9ac9 0%,#9a8a3c 45%,#6b5a2e 100%);}
  .photo-semi{background:linear-gradient(180deg,#6f9a5a 0%,#d8dde0 45%,#8c8a84 100%);}
  .photo-farm{background:linear-gradient(180deg,#a9c3da 0%,#c59a2a 50%,#5e4a33 100%);}
  .photo-atv{background:linear-gradient(180deg,#9a8a6e 0%,#3f5a42 50%,#2a2e2c 100%);}
  .photo-trailers{background:linear-gradient(180deg,#4f7a4a 0%,#d9d9d6 45%,#6a3a35 100%);}
  .brand{
    position:absolute;left:0;right:0;top:728px;text-align:center;
    font-family:"Archivo Black",sans-serif;font-weight:400;
    font-size:92px;line-height:1.02;color:#ffffff;letter-spacing:1px;
  }
  .site{
    position:absolute;left:0;right:0;top:960px;text-align:center;
    font-family:"Roboto",sans-serif;font-weight:700;font-size:34px;color:var(--orange);
  }
  .register{
    position:absolute;left:194px;top:1028px;width:812px;height:100px;box-sizing:border-box;
    border-radius:50px;border:4px solid #1e1e1e;
    background:linear-gradient(180deg,#f07a36 0%,var(--orange) 50%,var(--orange-deep) 100%);
    box-shadow:0 0 0 2px #555,0 8px 16px rgba(0,0,0,.5);
    display:flex;align-items:center;justify-content:center;text-decoration:none;
  }
  .register-text{
    font-family:"Archivo Black",sans-serif;font-size:64px;letter-spacing:1px;
    background:linear-gradient(180deg,#ffffff 0%,#dcdcdc 50%,#a5a5a5 100%);
    -webkit-background-clip:text;background-clip:text;color:transparent;
  }
  .pointer{position:absolute;left:960px;top:900px;width:110px;height:200px;}
</style>
</head>
<body>
<main class="ad">
  <h1 class="headline">RUN SALVAGE<br>AUCTION NOW!</h1>

  <svg class="chevrons" viewBox="0 0 52 312" aria-hidden="true">
    <g fill="none" stroke="var(--chevron)" stroke-width="9">
      <path d="M4 4 L26 24 L48 4"/><path d="M4 38 L26 58 L48 38"/>
      <path d="M4 72 L26 92 L48 72"/><path d="M4 106 L26 126 L48 106"/>
      <path d="M4 140 L26 160 L48 140"/><path d="M4 174 L26 194 L48 174"/>
      <path d="M4 208 L26 228 L48 208"/><path d="M4 242 L26 262 L48 242"/>
      <path d="M4 276 L26 296 L48 276"/>
    </g>
  </svg>

  <div class="card card-construction">
    <div class="card-photo photo-construction" role="img" aria-label="Yellow excavator on a dirt work site"></div>
    <div class="card-label">CONSTRUCTION EQPT</div>
  </div>
  <div class="card card-semi">
    <div class="card-photo photo-semi" role="img" aria-label="White semi truck parked on a gravel lot"></div>
    <div class="card-label">SEMI TRAILERS/TRUCKS</div>
  </div>
  <div class="card card-farm">
    <div class="card-photo photo-farm" role="img" aria-label="Yellow crawler dozer working in a muddy field"></div>
    <div class="card-label">FARM EQUIPMENT</div>
  </div>
  <div class="card card-atv">
    <div class="card-photo photo-atv" role="img" aria-label="Green side-by-side utility vehicle"></div>
    <div class="card-label">ATV/UTV - RVS</div>
  </div>
  <div class="card card-trailers">
    <div class="card-photo photo-trailers" role="img" aria-label="Flatbed trailer with loader crane"></div>
    <div class="card-label">TRAILERS - BOATS</div>
  </div>

  <div class="brand">CRIMSON<br>LEDGER</div>
  <div class="site">Crimson Ledger.com</div>

  <a class="register" href="https://www.crimsonledger.com/account/users/register">
    <span class="register-text">REGISTER FREE</span>
  </a>

  <svg class="pointer" viewBox="0 0 110 200" aria-hidden="true">
    <path d="M72 12 C110 60 100 140 30 178" fill="none" stroke="#c9c9c9" stroke-width="4" stroke-linecap="round"/>
    <path d="M30 178 L44 156 M30 178 L56 180" fill="none" stroke="#c9c9c9" stroke-width="4" stroke-linecap="round"/>
  </svg>
</main>
</body>
</html>
```